"Lantern Over Fields" Gospel Presentation Booklet

I need a design for a 12 page (including front/back cover) square booklet, with religious images and aesthetically pleasing fonts/designs. I want it to be very simple, and very straightforward. The main focus of the project is it's content. So the design should be very nice, but also should point to the content, not take away from it, or create distraction. People should be more focused on the words than the imagery.

I enjoy modern designs, I need a sharp aesthetic that is clean and neat. Nothing over the top.
I have attached a word document with the content I would like on the pages.

Colors
0592cd
0255a3
33a6d7
85cae6
85acd3
3276b5
9bcb3b
f04a50
f68d4c

Requirements
Should not have
• Super feminine colors/aesthetics

```html
<!DOCTYPE html>
<html lang="en">
<head>
<meta charset="utf-8">
<title>Lantern Over Fields — Booklet Spread</title>
<link href="https://fonts.googleapis.com/css2?family=Inter+Tight:wght@800&family=Lora:wght@400&display=swap" rel="stylesheet">
<style>
  :root {
    --backdrop: #e4e4e4;
    --sky-top: #dfe8ee;
    --sky-mid: #cde0ea;
    --sky-low: #c3dbe8;
    --ink: #111111;
    --text: #1e2226;
    --gutter: #c9d4da;
  }
  * { margin: 0; padding: 0; box-sizing: border-box; }
  html, body {
    width: 1200px;
    height: 900px;
    overflow: hidden;
    background: var(--backdrop);
  }
  .spread {
    position: absolute;
    left: 80px;
    top: 190px;
    width: 1040px;
    height: 520px;
    display: flex;
  }
  .page {
    position: relative;
    width: 520px;
    height: 520px;
    overflow: hidden;
  }
  .page + .page { border-left: 1px solid var(--gutter); }
  .sky {
    position: absolute;
    inset: 0;
    background:
      radial-gradient(ellipse 38% 22% at 45% 55%, rgba(255,255,255,0.85), rgba(255,255,255,0) 70%),
      radial-gradient(ellipse 30% 18% at 70% 20%, rgba(255,255,255,0.6), rgba(255,255,255,0) 70%),
      linear-gradient(to bottom, var(--sky-top) 0%, var(--sky-mid) 62%, var(--sky-low) 100%);
  }
  .title-word {
    position: absolute;
    left: 0;
    right: 0;
    top: 150px;
    text-align: center;
    font-family: "Inter Tight", "Arial Black", sans-serif;
    font-weight: 800;
    font-size: 230px;
    line-height: 1;
    letter-spacing: -4px;
    color: var(--ink);
  }
  .body-copy {
    position: absolute;
    left: 120px;
    top: 150px;
    font-family: "Lora", Georgia, serif;
    font-size: 23px;
    line-height: 1.32;
    color: var(--text);
  }
</style>
</head>
<body>
  <main class="spread">
    <section class="page page-left">
      <div class="sky" role="img" aria-label="Soft sky with white clouds over a calm sea"></div>
      <h1 class="title-word">MAN</h1>
    </section>
    <section class="page page-right">
      <div class="sky" role="img" aria-label="Soft sky with a white cloud over a calm sea"></div>
      <p class="body-copy">
        On the other hand,<br>
        mankind is corrupt.<br>
        For example,<br>
        we are selfish,<br>
        we are prideful,<br>
        and we lie.
      </p>
    </section>
  </main>
</body>
</html>
```